Upland Bird Hunting Preserve and Pointing Dog kennel

Need Price packages outlined for the bird hunting business. List the kennel and that we provide training and dogs for sale.
The preserve is "Tall Heron Expeditions" the dog kennel is "Pine Hollow Setters"
1/2 Day Upland Field Hunts: 5 Pheasants $120
7 Chukar $125
Continental Hunt 12 Pheasants $325 includes meal, minimum 12 hunters
Guides available $100

Target Market(s)

upland bird hunters

Industry/Entity Type

hunting, outdoor

Colors
EE7325
F08F49
F5BC92
FAE3D3
FDF4ED

```html
<!DOCTYPE html>
<html lang="en">
<head>
<meta charset="utf-8">
<title>Tall Heron Expeditions – Hunting Packages</title>
<link rel="stylesheet" href="https://fonts.googleapis.com/css2?family=Libre+Baskerville&family=Crimson+Text&display=swap">
<style>
  :root {
    --ink: #0d0d0d;
    --paper: #ffffff;
    --accent: #ee7325;
    --accent-mid: #f08f49;
    --accent-soft: #f5bc92;
    --accent-pale: #fae3d3;
    --backdrop: #fdf4ed;
  }
  * { margin: 0; padding: 0; box-sizing: border-box; }
  html, body { width: 1200px; height: 1200px; overflow: hidden; }
  body { background: var(--backdrop); position: relative; }
  .flyer {
    position: absolute; left: 133px; top: 0;
    width: 1292px; height: 1660px;
    transform: scale(0.7229); transform-origin: 0 0;
    background: var(--paper); color: var(--ink);
    font-family: "Crimson Text", "Times New Roman", serif;
  }
  .abs { position: absolute; white-space: nowrap; }
  .center-row { position: absolute; left: 0; width: 1292px; text-align: center; line-height: 1; white-space: nowrap; }
  .brand-title { top: 38px; font-family: "Libre Baskerville", Georgia, serif; font-size: 64px; }
  .brand-town { top: 112px; font-size: 46px; }
  .preserve-badge {
    left: 330px; top: 170px; width: 638px; height: 68px; border-radius: 6px;
    background: var(--accent); color: var(--paper); font-size: 52px;
    display: flex; align-items: center; justify-content: center;
  }
  .art { background: linear-gradient(160deg, var(--accent-pale), var(--accent-soft)); border-radius: 4px; }
  .art-hero { left: 390px; top: 265px; width: 520px; height: 370px; }
  .art-pheasant { left: 38px; top: 740px; width: 332px; height: 255px; }
  .art-chukar { left: 1015px; top: 740px; width: 145px; height: 235px; }
  .packages-heading { top: 660px; font-size: 60px; }
  .price-box {
    left: 432px; top: 742px; width: 192px; height: 105px;
    border: 2px solid var(--accent); border-radius: 7px; overflow: hidden;
    display: flex; flex-direction: column;
  }
  .price-box.chukar { left: 663px; }
  .price-label { height: 52px; font-size: 36px; display: flex; align-items: center; justify-content: center; }
  .price-value { flex: 1; background: var(--accent); color: var(--paper); font-size: 42px; display: flex; align-items: center; justify-content: center; }
  .guide-note {
    left: 410px; top: 875px; width: 465px; height: 40px;
    border-top: 2px solid var(--accent); border-bottom: 2px solid var(--accent);
    font-size: 31px; display: flex; align-items: center; justify-content: center;
  }
  .section-head { display: flex; justify-content: center; align-items: center; gap: 10px; font-size: 40px; }
  .section-head svg { width: 68px; height: 10px; color: var(--accent); }
  .detail { font-size: 31px; }
  .contact-name { left: 38px; top: 1484px; font-size: 32px; line-height: 1; }
  .contact-phone { left: 38px; top: 1522px; font-size: 52px; line-height: 1; display: flex; align-items: center; gap: 10px; }
  .contact-phone svg { width: 36px; height: 36px; color: var(--accent); }
  .contact-rule { left: 38px; top: 1577px; width: 392px; height: 5px; background: var(--accent); }
  .contact-note { left: 38px; top: 1594px; font-size: 27px; line-height: 1; }
  .kennel-name { left: 880px; top: 1530px; width: 370px; text-align: center; font-size: 32px; letter-spacing: 1px; line-height: 1; }
  .kennel-rule { left: 920px; top: 1578px; width: 297px; height: 4px; background: var(--accent); }
  .kennel-town { left: 880px; top: 1594px; width: 370px; text-align: center; font-size: 30px; letter-spacing: 1px; line-height: 1; }
  .footer-band { left: 0; top: 1632px; width: 1292px; height: 28px; background: var(--accent); }
</style>
</head>
<body>
<div class="flyer">
  <div class="center-row brand-title">TALL HERON EXPEDITIONS, LLC</div>
  <div class="center-row brand-town">Millbrook, MO</div>
  <div class="abs preserve-badge">Licensed Shooting Preserve</div>

  <div class="abs art art-hero" role="img" aria-label="Engraved illustration of a hunter with a shotgun in a field as two pheasants flush"></div>

  <div class="center-row packages-heading">Hunting Packages - 1/2 Day Upland Field Hunts</div>

  <div class="abs art art-pheasant" role="img" aria-label="Engraved illustration of a pheasant in flight over brush"></div>
  <div class="abs art art-chukar" role="img" aria-label="Engraved illustration of a chukar perched on a rock"></div>

  <div class="abs price-box pheasant">
    <div class="price-label">5 Pheasants</div>
    <div class="price-value">$120</div>
  </div>
  <div class="abs price-box chukar">
    <div class="price-label">7 Chukar</div>
    <div class="price-value">$125</div>
  </div>

  <div class="abs guide-note">Guide Available $100 per half day</div>

  <div class="center-row section-head" style="top:940px">
    <svg viewBox="0 0 68 10"><polygon points="0,5 68,1 68,9" fill="currentColor"/></svg>
    <span>Continental Pheasant Hunt</span>
    <svg viewBox="0 0 68 10"><polygon points="0,1 0,9 68,5" fill="currentColor"/></svg>
  </div>
  <div class="center-row detail" style="top:988px">- 12 Hunter Minimum</div>
  <div class="center-row detail" style="top:1030px">- $325 per hunter, includes 12 birds per hunter &amp; meal</div>
  <div class="center-row detail" style="top:1071px">- All hunts include bird cleaning</div>
  <div class="center-row detail" style="top:1112px">- Lodging available, call for pricing</div>

  <div class="center-row section-head" style="top:1170px">
    <svg viewBox="0 0 68 10"><polygon points="0,5 68,1 68,9" fill="currentColor"/></svg>
    <span>Guided Spring Turkey Hunts</span>
    <svg viewBox="0 0 68 10"><polygon points="0,1 0,9 68,5" fill="currentColor"/></svg>
  </div>
  <div class="center-row detail" style="top:1223px">- 3 Day Hunt includes meals &amp; lodging $1600</div>

  <div class="center-row section-head" style="top:1285px">
    <svg viewBox="0 0 68 10"><polygon points="0,5 68,1 68,9" fill="currentColor"/></svg>
    <span>Guided Whitetail Deer Hunts- Rifle &amp; Archery</span>
    <svg viewBox="0 0 68 10"><polygon points="0,1 0,9 68,5" fill="currentColor"/></svg>
  </div>
  <div class="center-row detail" style="top:1335px">- 5 Day Hunt includes meals &amp; lodging $2750</div>
  <div class="center-row detail" style="top:1377px">- Lodging available, call for pricing</div>

  <div class="abs contact-name">Dale Whitaker</div>
  <div class="abs contact-phone">
    <svg viewBox="0 0 24 24" aria-hidden="true"><path fill="currentColor" d="M6.6 10.8a15.1 15.1 0 0 0 6.6 6.6l2.2-2.2a1 1 0 0 1 1-.25 11.4 11.4 0 0 0 3.6.57 1 1 0 0 1 1 1V20a1 1 0 0 1-1 1A17 17 0 0 1 3 4a1 1 0 0 1 1-1h3.5a1 1 0 0 1 1 1c0 1.25.2 2.45.57 3.57a1 1 0 0 1-.25 1z"/></svg>
    <span>555-014-2737</span>
  </div>
  <div class="abs contact-rule"></div>
  <div class="abs contact-note">Puppies, started dogs &amp; training!</div>

  <div class="abs kennel-name">PINE HOLLOW SETTERS</div>
  <div class="abs kennel-rule"></div>
  <div class="abs kennel-town">ASHFORD, MO</div>

  <div class="abs footer-band"></div>
</div>
</body>
</html>
```